Spring Exterior Painting Advertisement

Attached is the postcard that we used last year(file - brightquill_318939...vector....pdf.. The information contained will be the same except for it will be updated for use during the spring of 2023.

The second attachment (sept 2021mailer) is another design that we've used in the past.

```html
<!DOCTYPE html>
<html lang="en">
<head>
<meta charset="utf-8">
<title>Summit Painting – Spring Postcard</title>
<link rel="stylesheet" href="https://fonts.googleapis.com/css2?family=Gilda+Display&family=Raleway:wght@400&display=swap">
<style>
  :root {
    --green: #149c4a;
    --charcoal: #2e323a;
    --slate: #45474d;
    --paper: #f0f0f1;
    --white: #ffffff;
    --yellow: #f2ef1e;
    --stamp: #7fd69c;
    --rule: #c9cbd0;
    --photo-sky: #5aa7a8;
    --photo-house: #7b8a5a;
    --photo-lawn: #5f9a55;
  }
  * { margin: 0; padding: 0; box-sizing: border-box; }
  html, body { width: 1200px; height: 1000px; overflow: hidden; background: var(--white); }
  body { position: relative; font-family: "Gilda Display", Georgia, serif; color: var(--white); }
  .abs { position: absolute; }

  .postcard {
    position: absolute; left: 292px; width: 584px; height: 398px;
    background: var(--paper); overflow: hidden;
    box-shadow: 0 14px 22px rgba(0,0,0,0.10);
  }
  .postcard--front { top: 60px; }
  .postcard--back { top: 518px; height: 397px; }

  /* front */
  .brand-band { left: 0; top: 0; width: 308px; height: 98px; background: var(--green); }
  .brand-name { left: 33px; top: 26px; font-size: 13px; line-height: 16px; letter-spacing: 0.5px; }
  .brand-mark { left: 33px; top: 64px; width: 12px; height: 12px; background: var(--white); }
  .title-panel { left: 0; top: 98px; width: 308px; height: 267px; background: var(--charcoal); }
  .title-main { left: 33px; top: 136px; font-size: 56px; line-height: 1; letter-spacing: 1px; }
  .title-sub { left: 34px; top: 210px; font-size: 25px; letter-spacing: 1.5px; }
  .title-rule { left: 33px; top: 271px; width: 217px; height: 3px; background: var(--white); }
  .front-phone { left: 33px; top: 290px; font-size: 27px; }
  .front-web { left: 33px; top: 326px; font-size: 12.5px; letter-spacing: 0.3px; }
  .house-photo {
    left: 308px; top: 0; width: 276px; height: 280px;
    background: linear-gradient(180deg, var(--photo-sky) 0%, #9cc7c0 38%, var(--photo-house) 55%, var(--photo-lawn) 72%, #a8c3bd 100%);
  }
  .front-shapes { left: 0; top: 0; }
  .coupon-text { left: 406px; top: 248px; width: 148px; text-align: center; }
  .coupon-save { color: var(--yellow); font-size: 18px; line-height: 23px; }
  .coupon-code { font-size: 13px; line-height: 15px; margin-top: 4px; }
  .coupon-expire { font-size: 11px; margin-top: 6px; }

  /* back */
  .quote-band { left: 0; top: 0; width: 584px; height: 99px; background: var(--green); }
  .quote-panel { left: 0; top: 99px; width: 276px; height: 181px; background: var(--green); }
  .address-panel { left: 276px; top: 99px; width: 308px; height: 265px; background: var(--charcoal); }
  .quote-heading { left: 33px; top: 20px; font-size: 24px; line-height: 32px; }
  .stamp-box { left: 486px; top: 23px; width: 65px; height: 65px; border: 1.5px solid var(--stamp); }
  .quote-copy { left: 33px; top: 96px; width: 232px; font-size: 10.5px; line-height: 16px; }
  .service-list { list-style: none; font-size: 8.5px; line-height: 15px; text-transform: uppercase; }
  .service-list li { position: relative; padding-left: 17px; margin-bottom: 6px; }
  .service-list li::before {
    content: ""; position: absolute; left: 0; top: 2px;
    width: 10px; height: 10px; border-radius: 50%; background: var(--white);
  }
  .service-list--left { left: 33px; top: 191px; width: 120px; }
  .service-list--right { left: 158px; top: 191px; width: 112px; }
  .company-name { left: 33px; top: 301px; font-size: 17px; color: var(--charcoal); letter-spacing: 0.3px; }
  .company-address { left: 33px; top: 328px; font-family: "Raleway", Arial, sans-serif; font-size: 11px; line-height: 13px; color: var(--slate); }
  .address-line { left: 347px; width: 203px; height: 1px; background: var(--rule); }
  .back-phone { left: 347px; top: 298px; font-size: 26px; }
  .back-web { left: 347px; top: 333px; font-size: 12.5px; letter-spacing: 0.3px; }
</style>
</head>
<body>

<section class="postcard postcard--front">
  <div class="abs house-photo" role="img" aria-label="Photo of a green two-storey house with lit windows, lawn and wet driveway under a blue sky"></div>
  <div class="abs brand-band"></div>
  <div class="abs brand-name">SUMMIT<br>PAINTING</div>
  <div class="abs brand-mark"></div>
  <div class="abs title-panel"></div>
  <svg class="abs front-shapes" width="584" height="398" viewBox="0 0 584 398" aria-hidden="true">
    <rect x="308" y="280" width="276" height="85" fill="var(--paper)"/>
    <polygon points="308,280 380,280 308,365" fill="var(--charcoal)"/>
    <polygon points="406,270 480,245 554,270 554,365 406,365" fill="var(--slate)" opacity="0.94"/>
  </svg>
  <div class="abs title-main">SUMMIT</div>
  <div class="abs title-sub">PAINTING</div>
  <div class="abs title-rule"></div>
  <div class="abs front-phone">(555) 014-2290</div>
  <div class="abs front-web">www.summitpaintingco.com</div>
  <div class="abs coupon-text">
    <div class="coupon-save">SAVE<br>15%</div>
    <div class="coupon-code">COUPON CODE<br>‘EXT2023’</div>
    <div class="coupon-expire">Expire 15.05.2023</div>
  </div>
</section>

<section class="postcard postcard--back">
  <div class="abs quote-band"></div>
  <div class="abs quote-panel"></div>
  <div class="abs address-panel"></div>
  <svg class="abs" style="left:0;top:0" width="584" height="397" viewBox="0 0 584 397" aria-hidden="true">
    <polygon points="205,280 276,280 276,364" fill="var(--slate)"/>
  </svg>
  <h1 class="abs quote-heading" style="font-weight:400">Request Your<br>free Summit Quote</h1>
  <div class="abs stamp-box"></div>
  <p class="abs quote-copy">Summit Painting’s local team offers professional painting for your home’s exterior and interior surfaces. With over 19 years in business, we offer skillful workmanship backed by a three-year warranty.</p>
  <ul class="abs service-list service-list--left">
    <li>Pressure washing</li>
    <li>Exterior painting &amp; staining</li>
    <li>Cabinetry finishing</li>
  </ul>
  <ul class="abs service-list service-list--right">
    <li>Interior painting</li>
    <li>Carpentry</li>
    <li>Color consul - tations</li>
  </ul>
  <div class="abs company-name">SUMMIT PAINTING</div>
  <div class="abs company-address">18 Harbor Ln. Unit B<br>Lakeview, WI 53000</div>
  <div class="abs address-line" style="top:141px"></div>
  <div class="abs address-line" style="top:174px"></div>
  <div class="abs address-line" style="top:207px"></div>
  <div class="abs address-line" style="top:240px"></div>
  <div class="abs back-phone">(555) 014-2290</div>
  <div class="abs back-web">www.summitpaintingco.com</div>
</section>

</body>
</html>
```